Talbrook landscape Solutions Postcard

Landscape Company, but we mainly focus on hardscape construction like stone walls and walkways, as well as our tree pruning. irrigation, weekly maintenance
I want the front of the postcard to draw u into the images and the back to have basic information

Reason: I need the card to have a backside and now be able to be mailed. I also need the images switched out. As well as some new verbage

Target Market(s)

High end home owners

Industry/Entity Type

Landscaping

Font styles to use
Decorative
Script

Requirements
Must have
• OUR SERVICES to be listed on the back as well as
• call for a free estimate
• follow us on chatlane and clipwall and roomvy
• Coupon outline
• New Customers Receive
• 10% off
• your hardscape project
• Decorate font for title on front of the card and coupon offer
Nice to have
• The front of the card should have a few of our images taking up the whole cover with our logo LOOK AT THE BECKET IMAGE I attached. I am going for that look with the classic black

```html
<!DOCTYPE html>
<html lang="en">
<head>
<meta charset="utf-8">
<title>Talbrook landscape Solutions Postcard</title>
<link rel="stylesheet" href="https://fonts.googleapis.com/css2?family=Anton&family=Arimo:ital,wght@0,400;0,700;1,700&family=Pathway+Gothic+One&display=swap">
<style>
  :root {
    --gold: #e4a32e;
    --gold-light: #f2b440;
    --black: #111111;
    --white: #ffffff;
    --green: #4d9a35;
    --green-dark: #2f7a1f;
    --ink: #1a1a1a;
    --slot: #d6d6d6;
    --paper: #ffffff;
  }
  * { box-sizing: border-box; margin: 0; padding: 0; }
  html, body { width: 1200px; height: 547px; overflow: hidden; background: var(--paper); }
  body { position: relative; font-family: "Arimo", Arial, sans-serif; }

  .card { position: absolute; overflow: hidden; }

  /* ---------- Front ---------- */
  .front { left: 64px; top: 98px; width: 492px; height: 382px; }
  .front-photo {
    position: absolute; inset: 0;
    background:
      linear-gradient(180deg, #1d2a1a 0%, #2f4a24 35%, #6f6a5a 52%, #4a5a3a 70%, #2f4a22 100%);
  }
  .brand-banner {
    position: absolute; left: 16px; top: 0; width: 106px; height: 94px;
    background: var(--black);
    border: 2px solid var(--gold); border-top: none;
    clip-path: polygon(0 0, 100% 0, 100% 100%, 50% 86%, 0 100%);
    display: flex; flex-direction: column; align-items: center; justify-content: center;
    padding-bottom: 12px; color: var(--white);
  }
  .brand-name { font-family: "Arimo", Arial, sans-serif; font-weight: 400; letter-spacing: 2px; font-size: 15px; line-height: 1; }
  .brand-sub { font-family: "Arimo", Arial, sans-serif; font-size: 5px; letter-spacing: 1px; margin-top: 4px; }
  .brand-tag { font-family: "Arimo", Arial, sans-serif; font-size: 5px; letter-spacing: 1px; margin-top: 18px; }

  .headline { position: absolute; left: 258px; top: 20px; width: 220px; text-align: center; }
  .headline-top { font-family: "Pathway Gothic One", sans-serif; color: var(--white); font-size: 28px; line-height: 1; letter-spacing: 1px; }
  .headline-main { font-family: "Pathway Gothic One", sans-serif; color: var(--gold-light); font-size: 25px; line-height: 1; margin-top: 2px; letter-spacing: 0.5px; }

  .inset {
    position: absolute; border: 3px solid var(--white); border-radius: 8px;
    box-shadow: 0 2px 6px rgba(0,0,0,0.5);
  }
  .inset-bar { left: 340px; top: 148px; width: 140px; height: 66px; background: linear-gradient(135deg, #b87a44, #7a4a26 60%, #3a2a1a); }
  .inset-arbor { left: 242px; top: 186px; width: 140px; height: 66px; background: linear-gradient(160deg, #6b7a4a, #9a8a5a 60%, #b08a5a); }
  .inset-patio { left: 344px; top: 238px; width: 141px; height: 68px; background: linear-gradient(170deg, #6a8a5a, #c8b690 50%, #8a3a26); }

  .coupon {
    position: absolute; left: 0; right: 0; top: 323px; height: 59px;
    background: var(--gold);
    border-top: 1.5px dashed var(--black);
  }
  .coupon-badge {
    position: absolute; top: 6px; width: 66px; height: 53px;
    background: var(--black); color: var(--white);
    display: flex; flex-direction: column; align-items: center; justify-content: center;
    clip-path: polygon(0 0, 100% 0, 100% 100%, 50% 88%, 0 100%);
  }
  .coupon-badge .brand-name { font-size: 10px; letter-spacing: 1px; }
  .coupon-badge .brand-sub { font-size: 4px; margin-top: 3px; }
  .badge-left { left: 34px; }
  .badge-right { left: 389px; }
  .coupon-text {
    position: absolute; left: 120px; top: 20px;
    font-family: "Pathway Gothic One", sans-serif; font-size: 19px; color: var(--ink); letter-spacing: 0.5px;
  }
  .coupon-offer {
    position: absolute; left: 306px; top: 15px; width: 66px; height: 25px;
    background: var(--white); font-family: "Anton", sans-serif; font-size: 19px; line-height: 25px;
    text-align: center; color: var(--black);
  }

  /* ---------- Back ---------- */
  .back { left: 630px; top: 95px; width: 474px; height: 389px; background: var(--paper); }
  .back-panel { position: absolute; left: 0; top: 0; width: 242px; height: 389px; }
  .back-header {
    position: absolute; left: 0; top: 0; width: 242px; height: 95px;
    background: linear-gradient(180deg, #2a2420, #3a302a 60%, #201a16);
    display: flex; flex-direction: column; align-items: center; padding-top: 22px; color: var(--white);
  }
  .back-header .brand-name { font-size: 15px; }
  .back-header .brand-tag { margin-top: 14px; }

  .project-title { position: absolute; left: 16px; top: 106px; font-family: "Pathway Gothic One", sans-serif; line-height: 1; }
  .project-title .line-green { color: var(--green); font-size: 26px; display: block; }
  .project-title .line-black { color: var(--ink); font-size: 26px; display: block; margin-top: 1px; }

  .estimate-call { position: absolute; left: 186px; top: 107px; font-size: 8px; font-weight: 700; color: var(--ink); }
  .estimate-seal { position: absolute; left: 182px; top: 120px; width: 58px; height: 58px; }

  .services-band {
    position: absolute; left: 0; top: 159px; width: 150px; height: 19px;
    background: linear-gradient(90deg, var(--green) 0%, var(--green) 55%, rgba(77,154,53,0) 100%);
    color: var(--white); font-size: 11.5px; font-weight: 700; line-height: 19px; padding-left: 14px;
  }
  .services-list { position: absolute; left: 18px; top: 183px; width: 222px; list-style: none; }
  .services-list li {
    position: relative; padding-left: 10px; font-size: 10.5px; font-weight: 700; font-style: italic;
    color: var(--ink); line-height: 14px; margin-bottom: 1px;
  }
  .services-list li::before {
    content: ""; position: absolute; left: 0; top: 4px; width: 6px; height: 6px; background: var(--green);
  }

  .follow { position: absolute; left: 0; top: 272px; display: flex; align-items: center; gap: 6px; }
  .follow-label { background: var(--black); color: var(--white); font-size: 10px; font-weight: 700; height: 15px; line-height: 15px; padding: 0 6px 0 14px; }
  .follow-name { font-size: 8px; font-weight: 700; color: var(--ink); display: flex; align-items: center; gap: 2px; }
  .follow-name::before { content: ""; width: 7px; height: 7px; background: var(--green); display: inline-block; }

  .back-photo {
    position: absolute; left: 0; top: 305px; width: 242px; height: 84px;
    background: linear-gradient(180deg, #d8d8d8 0%, #8a8a8a 45%, #4a4a4a 75%, #9a9a9a 100%);
  }

  .stamp-box { position: absolute; left: 402px; top: 34px; width: 60px; height: 61px; background: var(--slot); }
  .address-box { position: absolute; left: 263px; top: 214px; width: 206px; height: 99px; background: var(--slot); }
</style>
</head>
<body>

<section class="card front">
  <div class="front-photo" role="img" aria-label="Garden with a tall fieldstone wall, lawn, patio umbrellas and a white pool house among trees"></div>

  <div class="brand-banner">
    <span class="brand-name">TALBROOK</span>
    <span class="brand-sub">LANDSCAPE SOLUTIONS</span>
    <span class="brand-tag">DESIGN • BUILD • MAINTAIN</span>
  </div>

  <div class="headline">
    <div class="headline-top">LET US CREATE YOUR</div>
    <div class="headline-main">OUTDOOR LVING SPACE</div>
  </div>

  <div class="inset inset-bar" role="img" aria-label="Stone outdoor bar with wooden stools"></div>
  <div class="inset inset-arbor" role="img" aria-label="Garden arbor over a brick paver walkway"></div>
  <div class="inset inset-patio" role="img" aria-label="Backyard patio with mulched beds and lawn"></div>

  <div class="coupon">
    <div class="coupon-badge badge-left">
      <span class="brand-name">TALBROOK</span>
      <span class="brand-sub">LANDSCAPE SOLUTIONS</span>
    </div>
    <div class="coupon-text">NEW CUSTOMERS RECEIVE -</div>
    <div class="coupon-offer">10% OFF</div>
    <div class="coupon-badge badge-right">
      <span class="brand-name">TALBROOK</span>
      <span class="brand-sub">LANDSCAPE SOLUTIONS</span>
    </div>
  </div>
</section>

<section class="card back">
  <div class="back-panel">
    <div class="back-header" role="img" aria-label="Dim photo of a stone outdoor structure with the company name">
      <span class="brand-name">TALBROOK</span>
      <span class="brand-sub">LANDSCAPE SOLUTIONS</span>
      <span class="brand-tag">DESIGN • BUILD • MAINTAIN</span>
    </div>

    <h1 class="project-title">
      <span class="line-green">YOUR HARDSCAPE</span>
      <span class="line-black">PROJECT</span>
    </h1>

    <div class="estimate-call">CALL FOR A</div>
    <svg class="estimate-seal" viewBox="0 0 58 58" aria-label="Free estimate">
      <polygon fill="var(--green)" points="29,1 33,6 39,3 41,9 48,8 48,15 54,17 51,23 57,29 51,35 54,41 48,43 48,50 41,49 39,55 33,52 29,57 25,52 19,55 17,49 10,50 10,43 4,41 7,35 1,29 7,23 4,17 10,15 10,8 17,9 19,3 25,6"/>
      <circle cx="29" cy="29" r="19" fill="var(--green-dark)" stroke="#ffffff" stroke-width="1"/>
      <text x="29" y="28" text-anchor="middle" font-family="Pathway Gothic One, sans-serif" font-size="11" fill="#ffffff">FREE</text>
      <text x="29" y="37" text-anchor="middle" font-family="Pathway Gothic One, sans-serif" font-size="7" fill="#ffffff">ESTIMATE</text>
    </svg>

    <div class="services-band">Services we offer</div>
    <ul class="services-list">
      <li>Landscaping</li>
      <li>Hardscape construction like stone walls and Walkways</li>
      <li>as well as our Tree Pruning</li>
      <li>Irrigation</li>
      <li>Weekly maintenance</li>
    </ul>

    <div class="follow">
      <span class="follow-label">Follow us on</span>
      <span class="follow-name">chatlane</span>
      <span class="follow-name">clipwall</span>
      <span class="follow-name">roomvy</span>
    </div>

    <div class="back-photo" role="img" aria-label="Black and white photo of a circular stone fire pit patio beside tall grasses"></div>
  </div>

  <div class="stamp-box"></div>
  <div class="address-box"></div>
</section>

</body>
</html>
```